Business card design for Allied Healthcare provider

We would like a design for front and back of business cards. The design must resonate with all levels of customers from patients, to other health providers and medical. Must also resonate with corporate customers

Target Market(s)

patients, medical practitioners, other health providers and corporate.

Industry/Entity Type

healthcare

Contact Information for Business Card

name, logo, phone and fax numbers, email, website

Requirements
Must have
• not allowing me to change this, but the card must be double sided!! Please take note
Nice to have
• a fresh yet bold design to catch attention.

```html
<!DOCTYPE html>
<html lang="en">
<head>
<meta charset="UTF-8">
<title>Carevale Business Card – Front and Back</title>
<link rel="stylesheet" href="https://fonts.googleapis.com/css2?family=Montserrat:wght@500;600;700&family=Open+Sans:wght@500;600&display=swap">
<style>
  :root {
    --navy: #1b2c57;
    --gold: #fbb52b;
    --paper: #ffffff;
    --backdrop: #d1d2d4;
    --muted: #6d6e71;
    --shadow: rgba(60, 60, 60, 0.45);
  }
  * { margin: 0; padding: 0; box-sizing: border-box; }
  html, body { width: 1200px; height: 1044px; overflow: hidden; }
  body {
    background: var(--backdrop);
    font-family: "Montserrat", sans-serif;
    position: relative;
  }
  .card {
    position: absolute;
    left: 341px;
    width: 540px;
    height: 305px;
    overflow: hidden;
    box-shadow: 7px 9px 10px var(--shadow);
  }
  .card-front { top: 171px; background: var(--paper); border: 1px solid #b9babc; }
  .card-back { top: 536px; background: var(--navy); }

  .brand {
    position: absolute;
    display: flex;
    align-items: center;
    gap: 8px;
    font-weight: 700;
    font-size: 25px;
    letter-spacing: -0.3px;
  }
  .brand-dot {
    width: 26px; height: 26px;
    border-radius: 50%;
    background: var(--gold);
  }
  .card-front .brand { left: 32px; top: 62px; color: var(--navy); }
  .card-back .brand { left: 0; right: 0; top: 103px; justify-content: center; color: var(--paper); }

  .side-band { position: absolute; right: 0; top: 0; width: 30px; height: 100%; }

  .role {
    position: absolute;
    right: 32px;
    top: 116px;
    text-align: right;
    font-size: 13px;
    letter-spacing: 1.4px;
    line-height: 20px;
  }
  .role-title { font-weight: 700; color: var(--navy); }
  .role-sub { font-weight: 500; color: var(--muted); }

  .contact-list {
    position: absolute;
    right: 32px;
    top: 201px;
    list-style: none;
    font-size: 16px;
    font-weight: 500;
    color: var(--muted);
    letter-spacing: 0.6px;
  }
  .contact-list li {
    display: flex;
    align-items: center;
    justify-content: flex-end;
    gap: 10px;
    height: 26px;
  }
  .contact-list svg { width: 15px; height: 15px; }

  .tab {
    position: absolute;
    bottom: 0;
    left: 109px;
    width: 323px;
    height: 44px;
    display: flex;
    align-items: center;
    justify-content: center;
    gap: 12px;
  }
  .tab-shape { position: absolute; inset: 0; width: 100%; height: 100%; z-index: 0; }
  .tab > *:not(.tab-shape) { position: relative; z-index: 1; }
  .tab-email { font-size: 17px; font-weight: 500; color: var(--gold); letter-spacing: 0.4px; }
  .tab-address { font-family: "Open Sans", sans-serif; font-size: 17px; font-weight: 600; color: var(--navy); }
  .tab svg.icon { width: 16px; height: 16px; }
</style>
</head>
<body>

  <section class="card card-front" aria-label="Business card front">
    <div class="brand"><span class="brand-dot"></span>carevale</div>

    <svg class="side-band" viewBox="0 0 30 305" preserveAspectRatio="none" aria-hidden="true">
      <rect x="8" y="0" width="22" height="305" fill="var(--navy)"/>
      <polygon points="8,105 18,118 8,131" fill="var(--paper)"/>
    </svg>

    <div class="role">
      <div class="role-title">ALLIED HEALTHCARE</div>
      <div class="role-sub">PROVIDER</div>
    </div>

    <ul class="contact-list">
      <li>(999) 222-5555
        <svg viewBox="0 0 16 16" aria-hidden="true"><rect x="4" y="1" width="8" height="14" rx="1.5" fill="none" stroke="var(--gold)" stroke-width="1.6"/><line x1="7" y1="12.5" x2="9" y2="12.5" stroke="var(--gold)" stroke-width="1.4"/></svg>
      </li>
      <li>www.ssssss.com
        <svg viewBox="0 0 16 16" aria-hidden="true"><circle cx="8" cy="8" r="6.5" fill="none" stroke="var(--gold)" stroke-width="1.5"/><ellipse cx="8" cy="8" rx="3" ry="6.5" fill="none" stroke="var(--gold)" stroke-width="1.2"/><line x1="1.5" y1="8" x2="14.5" y2="8" stroke="var(--gold)" stroke-width="1.2"/></svg>
      </li>
    </ul>

    <div class="tab">
      <svg class="tab-shape" viewBox="0 0 323 44" preserveAspectRatio="none" aria-hidden="true">
        <polygon points="13,0 310,0 323,44 0,44" fill="var(--navy)"/>
      </svg>
      <svg class="icon" viewBox="0 0 16 16" aria-hidden="true"><rect x="1" y="3" width="14" height="10" fill="var(--gold)"/><polyline points="1,3 8,9 15,3" fill="none" stroke="var(--navy)" stroke-width="1.3"/></svg>
      <span class="tab-email">aaaaaaa@nnn.com</span>
    </div>
  </section>

  <section class="card card-back" aria-label="Business card back">
    <div class="brand"><span class="brand-dot"></span>carevale</div>

    <div class="tab">
      <svg class="tab-shape" viewBox="0 0 323 44" preserveAspectRatio="none" aria-hidden="true">
        <polygon points="10,0 313,0 323,44 0,44" fill="var(--gold)"/>
      </svg>
      <svg class="icon" viewBox="0 0 16 16" aria-hidden="true"><path d="M8 1a5 5 0 0 0-5 5c0 4 5 9 5 9s5-5 5-9a5 5 0 0 0-5-5z" fill="var(--navy)"/><circle cx="8" cy="6" r="2" fill="var(--gold)"/></svg>
      <span class="tab-address">City, State Name, 77</span>
    </div>
  </section>

</body>
</html>
```